Flyer PRTW

Everyone deserves true happiness.
Real Food is the answer to:
A body you love
Reverting illnesses
Healthy digestion
Stable blood sugar
Emotions in control
Blasting energy
Sound sleep
REAL food + water + exercise + Laughter =
“HIGH QUALITY OF LIFE “
EASY, right?
Challenging: certainly
Changing habits: reluctance in sight!
WE’RE OFFER TO:
1. Study YOUR unique body composition, food cravings, blockages, illnesses, and personality!
2. Introduce you to new Food
3. customized wellness plan with follow ups
4. meditation,cooking, and fitness classes as well as wellness workshops
5. New friends with high aspirations
LOGO
Contact info
Please visit our web address to see our design style and colors: www.pinerivertallwave.net
Target Market(s)
people who want to be more healthy
Industry/Entity Type
Fitness
Requirements
Must have
- beautiful pictures of fresh food (main picture) and maybe a few more small pictures reflecting
exercise
healthy living
meditation
Nice to have
- look is crucial. recall some of the color or colors from my logo to have a theme

```html
<!DOCTYPE html>
<html lang="en">
<head>
<meta charset="utf-8">
<title>Pinerivertallwave Flyer</title>
<link href="https://fonts.googleapis.com/css2?family=Oswald:wght@400;500;600&display=swap" rel="stylesheet">
<style>
  :root{
    --stage:#ecebe6;
    --paper:#ffffff;
    --cream:#fdf1e2;
    --orange:#f07c12;
    --orange-deep:#e36a0a;
    --yellow:#f7c415;
    --green:#5aa62b;
    --green-dark:#3f8a1d;
    --ink:#2b2b2b;
    --grey:#4a4a4a;
  }
  *{margin:0;padding:0;box-sizing:border-box}
  html,body{width:1200px;height:900px;overflow:hidden}
  body{background:var(--stage);font-family:"Oswald",sans-serif;color:var(--ink)}
  .flyer{position:absolute;left:290px;top:30px;width:620px;height:840px;background:var(--paper);overflow:hidden;box-shadow:0 6px 24px rgba(0,0,0,.18)}
  .flyer-shapes{position:absolute;inset:0}
  .brand{position:absolute;left:22px;top:16px;display:flex;align-items:center;gap:10px}
  .brand-dot{width:42px;height:42px;border-radius:50%;background:var(--green)}
  .brand-name{font-size:25px;font-weight:600;color:var(--grey);line-height:1}
  .brand-tag{font-size:7.5px;letter-spacing:.6px;color:var(--green-dark);margin-top:4px;font-weight:500}
  .tagline{position:absolute;right:22px;top:17px;color:#fff;font-size:18px;font-weight:400}
  .photo{position:absolute}
  .formula{position:absolute;left:18px;top:272px;color:var(--green-dark);font-size:19px;font-weight:600;line-height:1.2}
  .section-title{position:absolute;color:var(--green);font-size:19px;font-weight:600;letter-spacing:.3px}
  .benefits{position:absolute;left:40px;top:420px;width:540px;display:grid;grid-template-columns:190px 175px 175px;row-gap:2px;list-style:none}
  .benefits li{font-size:19px;font-weight:500;color:var(--ink);position:relative;padding-left:16px}
  .benefits li::before{content:"";position:absolute;left:0;top:11px;width:8px;height:8px;border-radius:50%;background:var(--ink)}
  .services{position:absolute;left:40px;top:560px;width:540px;list-style:none;counter-reset:step}
  .services li{font-size:17px;font-weight:400;line-height:1.32;padding-left:18px;text-indent:-18px}
  .website{position:absolute;right:34px;top:712px;color:var(--green);font-size:19px;font-weight:600}
  .contact{position:absolute;left:80px;top:796px;display:flex;align-items:center;gap:12px;color:var(--green-dark);font-size:20px;font-weight:500}
</style>
</head>
<body>
<main class="flyer">
  <svg class="flyer-shapes" viewBox="0 0 620 840" width="620" height="840" aria-hidden="true">
    <defs>
      <linearGradient id="photoTone" x1="0" y1="0" x2="1" y2="1">
        <stop offset="0" stop-color="#7fb83a"/>
        <stop offset=".45" stop-color="#b9d77a"/>
        <stop offset=".75" stop-color="#d8493a"/>
        <stop offset="1" stop-color="#5c8f2a"/>
      </linearGradient>
      <linearGradient id="sunBand" x1="0" y1="0" x2="1" y2="0">
        <stop offset="0" stop-color="var(--orange-deep)"/>
        <stop offset="1" stop-color="var(--yellow)"/>
      </linearGradient>
      <linearGradient id="banner" x1="0" y1="0" x2="1" y2="0">
        <stop offset="0" stop-color="#fbd43a"/>
        <stop offset="1" stop-color="var(--orange)"/>
      </linearGradient>
      <radialGradient id="glow" cx=".55" cy=".15" r=".9">
        <stop offset="0" stop-color="#fffaf2"/>
        <stop offset="1" stop-color="var(--cream)"/>
      </radialGradient>
      <linearGradient id="footerBand" x1="0" y1="0" x2="0" y2="1">
        <stop offset="0" stop-color="#fff6cf"/>
        <stop offset="1" stop-color="var(--yellow)"/>
      </linearGradient>
    </defs>
    <!-- tagline tab -->
    <path d="M300 8 H620 V52 H300 L286 30 Z" fill="url(#sunBand)"/>
    <!-- body -->
    <rect x="0" y="330" width="620" height="510" fill="url(#glow)"/>
    <!-- orange sweep over photo -->
    <path d="M0 70 H620 V82 C420 88 200 110 0 170 Z" fill="url(#sunBand)"/>
    <!-- green swoosh under photo -->
    <path d="M0 370 C200 330 420 318 620 322 V340 C420 340 200 355 0 395 Z" fill="var(--green)"/>
    <!-- formula banner -->
    <path d="M0 262 H322 L338 296 L322 330 H0 Z" fill="url(#banner)"/>
    <!-- bottom orange band -->
    <path d="M0 785 C220 770 430 735 620 680 V720 C430 770 220 800 0 808 Z" fill="url(#sunBand)"/>
    <!-- footer -->
    <path d="M0 808 C220 800 430 770 620 720 V840 H0 Z" fill="url(#footerBand)"/>
    <path d="M0 815 C220 807 430 778 620 730" stroke="#fff" stroke-width="3" fill="none"/>
  </svg>

  <div class="photo" role="img" aria-label="Photograph of a fresh Greek salad with lettuce, cucumber, tomatoes, olives and feta"
       style="left:0;top:118px;width:620px;height:218px;clip-path:polygon(0 28%,30% 10%,65% 3%,100% 0,100% 100%,0 100%);background:linear-gradient(135deg,#7fb83a,#b9d77a 40%,#d8493a 70%,#5c8f2a);z-index:0"></div>

  <div class="brand">
    <span class="brand-dot"></span>
    <div>
      <div class="brand-name">Pinerivertallwave</div>
      <div class="brand-tag">BALANCED NUTRITION, MIND, AND FITNESS</div>
    </div>
  </div>
  <p class="tagline">Everyone deserves true happiness.</p>

  <svg class="flyer-shapes" viewBox="0 0 620 840" width="620" height="840" aria-hidden="true" style="pointer-events:none">
    <path d="M0 262 H322 L338 296 L322 330 H0 Z" fill="url(#banner)"/>
  </svg>
  <p class="formula">REAL food + water + exercise + L.O.L. =<br>“HIGH QUALITY OF LIFE“</p>

  <h2 class="section-title" style="left:40px;top:388px">REAL FOOD IS THE ANSWER TO:</h2>
  <ul class="benefits">
    <li>Reverting illnesses</li><li>A body you love</li><li>Stable blood sugar</li>
    <li>Emotions in control</li><li>Healthy digestion</li><li>Sound sleep</li>
    <li style="visibility:hidden">.</li><li>Blasting energy</li>
  </ul>

  <h2 class="section-title" style="left:40px;top:530px">WE’RE HERE TO:</h2>
  <ol class="services">
    <li>1. Study YOUR unique body composition, food cravings, blockages, illnesses, and personality!</li>
    <li>2. Educate – guide – develop plan – and follow you up 24/7</li>
    <li>3. You will: taste new food, plan meals, groceries shopping.</li>
    <li>4. You’ll attend: meditation, cooking, and fitness classes</li>
    <li>5. You’ll make new friends</li>
  </ol>

  <p class="website">www.pinerivertallwave.net</p>
  <p class="contact">
    <svg width="26" height="22" viewBox="0 0 26 22" aria-hidden="true">
      <path d="M2 7 C6 1 20 1 24 7 L20 10 L17 6 H9 L6 10 Z" fill="var(--green-dark)"/>
      <rect x="6" y="10" width="14" height="10" rx="2" fill="var(--green-dark)"/>
      <circle cx="13" cy="15" r="3" fill="#fff6cf"/>
    </svg>
    (555) 210-4836
  </p>
</main>
</body>
</html>
```